Flyer needed for Seminar

Hello,
We are looking for eye-catching, inspiring marketing material for an educational seminar. We need 4 x 6 clubcards with the following info:

CLUBCARD FRONT:

Valtren Academy Presents:

Prayer: Past The Habit
Unlock the hidden treasures of prayer
By. Shaykh Idris Kamal Al-Tarifi

Dates:Jan 23-25, 2015
Timings: Fri - 7pm - 9:30 pm; Sat/Sun - 9am - 8 pm

Location: Dallas/Plano Corvane Suites at Ridgefield Commons
4830 Mercer Lane, Plano, TX 75093

Seating is Limited. Register Today!
www.ValtrenAcademy,example

CLUBCARD BACK:
In this unique seminar, learn how to connect spiritually with your Creator through prayer. Let us teach you the hidden meanings behind salah and why it is essential to your existence. Not only will the instructor impart the skills you'll need to master khushoo but he will delve more deeply, into the inner realms and intricacies of this ibadaa. As a result, the prayer will no longer be regarded as a mechanical chore, but an intimate meeting with the Divine. Through such insight, we hope you will leave this non-fiqh seminar with an awakened and unparalleled understanding of this fundamental pillar of Islam.

www.ValtrenAcademy.example
For more info: Email - info@valtrenacademy.example; Phone - 1-877-Valtren

Reason: I really appreciate all the submissions but am looking for something more eye-catching, something that really stirs ones interest and relates to the title of the seminar. Thank you!

```html
<!DOCTYPE html>
<html lang="en">
<head>
<meta charset="utf-8">
<title>Prayer: Past The Habit – Seminar Card Back</title>
<link rel="stylesheet" href="https://fonts.googleapis.com/css2?family=Alegreya:wght@400&family=Raleway:wght@400&display=swap">
<style>
  :root {
    --frame-gold: #EDCB6A;
    --title-gold: #A88F45;
    --body-gold: #B79A57;
    --ink-dark: #4A3F28;
    --footer-grey: #7A7A7A;
    --link-gold: #D9A72E;
    --ornament-tint: #F6EFD6;
    --paper: #FFFFFF;
  }
  * { margin: 0; padding: 0; box-sizing: border-box; }
  html, body { width: 800px; height: 1200px; overflow: hidden; background: var(--paper); }
  .card {
    position: relative;
    width: 800px; height: 1200px;
    background: var(--paper);
    border: 22px solid var(--frame-gold);
    font-family: "Alegreya", Georgia, serif;
    text-align: center;
  }
  .ornament-field {
    position: absolute;
    left: 8px; top: 298px;
    width: 740px; height: 560px;
    background: radial-gradient(ellipse 50% 50% at 50% 50%, var(--ornament-tint) 0%, rgba(246,239,214,0.55) 55%, rgba(255,255,255,0) 100%);
  }
  .seminar-title {
    position: absolute;
    left: 0; right: 0; top: 213px;
    color: var(--title-gold);
    font-family: "Alegreya", Georgia, serif;
    font-weight: 400;
    font-size: 60px;
    line-height: 60px;
  }
  .intro-lead {
    position: absolute; left: 0; right: 0; top: 391px;
    font-size: 29px; line-height: 34px; color: var(--ink-dark);
  }
  .intro-body {
    position: absolute; left: 0; right: 0; top: 470px;
    font-size: 25.5px; line-height: 30px; color: var(--body-gold);
  }
  .contact {
    position: absolute; left: 0; right: 0; top: 891px;
    font-size: 24.5px; line-height: 30.5px; color: var(--ink-dark);
  }
  .footer-line {
    position: absolute; left: 0; right: 0; top: 1104px;
    font-family: "Raleway", Arial, sans-serif;
    font-size: 22px; line-height: 26px; color: var(--footer-grey);
  }
  .footer-line .site { color: var(--link-gold); }
</style>
</head>
<body>
  <main class="card">
    <div class="ornament-field" role="img" aria-label="Faint cream arabesque ornament behind the description text"></div>

    <h1 class="seminar-title">Past The Habit</h1>

    <p class="intro-lead">In this unique seminar, learn how to connect<br>spiritually with your Creator through prayer.</p>

    <p class="intro-body">Let us teach you the hidden meanings behind salah<br>and why it is essential to your existence. Not only<br>will the instructor impart the skills you'll need to<br>master khushoo but he will delve more deeply, into<br>the inner realms and intricacies of this ibadaa.<br>As a result, the prayer will no longer be regarded as a<br>mechanical chore, but an intimate meeting with the<br>Divine. Through such insight, we hope you will leave<br>this non-fiqh seminar with an awakened and<br>unparalleled understanding of this fundamental<br>pillar of Islam.</p>

    <p class="contact">For more info:<br>Email - info@valtrenacademy.example<br>Phone - 1-877-Valtren</p>

    <p class="footer-line">Seating is Limited. Register Today! |&nbsp; <span class="site">www.ValtrenAcademy.example</span></p>
  </main>
</body>
</html>
```